Etiketten für Wein und Sekt
Zielgruppe
Sekt- und Weinherstellung
Zielgruppe 25 - 60 Jahre
Aufgabenstellung
Wir führen ein neues Produkt in den Markt ein:
gewünschter Name: The Velvet Orchard Taste
Hervorgehoben werden soll 'Velvet Orchard'
auf dieser Basis suchern wir einmal das Etikett für den WEIN
und einmal das Etikett für den SEKT (gleiches Design/Designfamilie)
Beim Sekt dachten wir an den Zusatz Sparkling auf dem Etikett?
Achtung, es handelt sich hier um keinen Eiswein !
Damit darf unser Produkt nicht in Verbindung gebracht werden (dt. Weinrecht)
Unser Wein/Sekt ist ein fruchtiger Rose Wein/Sekt
Ein Cuvée aus regionalen Rebsorten
Beim Trinkgenuss sollen die Gedanken an gefrorene Beeren/Trauben gehen.
Wir dachten an Beerentöne und Rosegold (wie der Inhalt)
Aktuell verwenden wir Etikettenformen in Rechteckgröße horizontal oder vertikal
Besten Dank im Voraus !!

```html
<!DOCTYPE html>
<html lang="de">
<head>
<meta charset="utf-8">
<title>The Velvet Orchard Taste – Weinetikett</title>
<link rel="stylesheet" href="https://fonts.googleapis.com/css2?family=Open+Sans:wght@400;700&display=swap">
<style>
  :root {
    --berry-dark: #3a2f4f;
    --berry-blue: #5b5f86;
    --berry-pink: #c97a8e;
    --berry-red: #8e3a4e;
    --frost: rgba(236, 232, 240, 0.82);
    --frame-purple: #8a12c4;
    --frame-deep: #5a0a8a;
    --title-purple: #9a1bd0;
    --white: #ffffff;
  }
  html, body {
    margin: 0;
    padding: 0;
    width: 923px;
    height: 1200px;
    overflow: hidden;
    background: #ffffff;
  }
  .label {
    position: relative;
    width: 923px;
    height: 1200px;
    overflow: hidden;
    font-family: "Open Sans", sans-serif;
  }
  .berry-photo {
    position: absolute;
    inset: 0;
    background:
      radial-gradient(circle at 15% 18%, #9c9ab8 0 14%, transparent 30%),
      radial-gradient(circle at 62% 12%, #d9909e 0 12%, transparent 28%),
      radial-gradient(circle at 12% 82%, #e39aae 0 14%, transparent 30%),
      radial-gradient(circle at 90% 55%, #e48894 0 10%, transparent 24%),
      radial-gradient(circle at 38% 48%, var(--berry-red) 0 8%, transparent 22%),
      radial-gradient(circle at 85% 88%, #707399 0 12%, transparent 28%),
      linear-gradient(160deg, var(--berry-blue), var(--berry-dark) 55%, var(--berry-pink));
  }
  .frost {
    position: absolute;
    inset: 0;
    background: radial-gradient(ellipse 62% 58% at 50% 48%, var(--frost) 0%, rgba(236,232,240,0.55) 55%, rgba(236,232,240,0.1) 100%);
  }
  .frame-outer {
    position: absolute;
    inset: 4px;
    border: 14px solid var(--frame-purple);
    box-shadow: inset 0 0 0 2px var(--frame-deep), 0 0 0 2px var(--frame-deep);
  }
  .frame-inner {
    position: absolute;
    inset: 33px;
    border: 4px solid var(--frame-purple);
  }
  .line {
    position: absolute;
    left: 0;
    right: 0;
    margin: 0;
    text-align: center;
    line-height: 1;
    transform: translateY(-50%);
  }
  .title-line {
    font-weight: 700;
    color: var(--title-purple);
  }
  .title-the   { top: 286px; font-size: 66px; }
  .title-main  { top: 429px; font-size: 86px; }
  .title-taste { top: 562px; font-size: 66px; }
  .vintage {
    top: 839px;
    font-weight: 700;
    font-size: 60px;
    color: var(--white);
  }
  .variety {
    top: 996px;
    font-weight: 400;
    font-size: 60px;
    color: var(--white);
  }
  .cuvee {
    top: 1110px;
    font-weight: 400;
    font-size: 46px;
    color: var(--title-purple);
  }
</style>
</head>
<body>
  <main class="label">
    <div class="berry-photo" role="img" aria-label="Nahaufnahme gefrorener Himbeeren und Brombeeren mit Raureif"></div>
    <div class="frost"></div>
    <div class="frame-outer"></div>
    <div class="frame-inner"></div>

    <h1 class="title">
      <span class="line title-line title-the">The</span>
      <span class="line title-line title-main">Velvet Orchard</span>
      <span class="line title-line title-taste">Taste</span>
    </h1>

    <p class="line vintage">2023</p>
    <p class="line variety">Rose</p>
    <p class="line cuvee">Cuvée aus regionalen Rebsorten</p>
  </main>
</body>
</html>
```